FOLI PACK FOR STICKS

Design the packaging for salted sticks (weight 400g) reference to the logo VOLK (in attached).
Color packaging- look forward to suggestions.
Package with window.
Hi, we need only graphic conception without texts on back side.

Please find Logo VOLK and the grid of packaging - attached
Updates

Target Market(s)

typical salted snack for everyone (adults and children included)

Font styles to use
Sans Serif

Requirements
Should not have
• - religion and politic signs…
• - toys and childdraws
• - monsters, devils and demons etc.

```html
<!DOCTYPE html>
<html lang="en">
<head>
<meta charset="utf-8">
<title>VOLK Salted Pretzel Sticks – Pack Front</title>
<link rel="stylesheet" href="https://fonts.googleapis.com/css2?family=Alegreya:ital,wght@1,500&family=Cabin:wght@500;700&display=swap">
<style>
  :root {
    --paper: #ffffff;
    --brand-brown: #5c3d1c;
    --tagline: #8a7b69;
    --label-grey: #8f8474;
    --weight-brown: #5e3a1e;
    --glow: rgba(255, 236, 190, 0.85);
    --pretzel-light: #e0842c;
    --pretzel-dark: #9a4a12;
    --window-rim: #a5805a;
  }
  html, body {
    margin: 0;
    padding: 0;
    width: 1200px;
    height: 1000px;
    overflow: hidden;
    background: var(--paper);
  }
  .canvas {
    position: relative;
    width: 1200px;
    height: 1000px;
    background: var(--paper);
  }
  .landscape-artwork {
    position: absolute;
    left: 10px;
    top: 99px;
    width: 1180px;
    height: 722px;
    background:
      radial-gradient(ellipse 45% 30% at 50% 2%, rgba(240,230,215,0.9) 0%, rgba(240,230,215,0) 100%),
      radial-gradient(ellipse 35% 25% at 50% 56%, rgba(236,220,196,0.55) 0%, rgba(236,220,196,0) 100%),
      radial-gradient(ellipse 30% 22% at 0% 100%, rgba(80,60,45,0.55) 0%, rgba(80,60,45,0) 100%),
      linear-gradient(180deg,
        #d6c8b5 0%, #d0c0aa 17%,
        #a8927a 21%, #9d866d 25%, #b8a389 28%,
        #c6b39b 33%, #b29c82 38%, #c4b098 43%,
        #ae977c 49%, #c2ae95 54%, #b09a80 60%,
        #c0ac93 66%, #a68f75 73%, #bca78e 79%,
        #a38c72 86%, #b19b81 92%, #9a836b 100%);
  }
  .spec-panel {
    position: absolute;
    background: var(--paper);
    border-radius: 12px;
  }
  .spec-panel--left  { left: 40px;  top: 221px; width: 153px; height: 471px; }
  .spec-panel--right { left: 978px; top: 226px; width: 152px; height: 470px; }
  .brand-name {
    position: absolute;
    left: 0;
    width: 1200px;
    top: 272px;
    text-align: center;
    font-family: "Cabin", sans-serif;
    font-weight: 700;
    font-size: 66px;
    line-height: 1;
    letter-spacing: 1px;
    color: var(--brand-brown);
  }
  .tagline-arc {
    position: absolute;
    left: 0;
    top: 0;
    width: 1200px;
    height: 1000px;
  }
  .tagline-arc text {
    font-family: "Alegreya", serif;
    font-style: italic;
    font-weight: 500;
    font-size: 42px;
    fill: var(--tagline);
  }
  .product-window {
    position: absolute;
    left: 436px;
    top: 425px;
    width: 320px;
    height: 154px;
    border-radius: 50%;
    border: 2px solid var(--window-rim);
    box-sizing: border-box;
    background:
      repeating-linear-gradient(62deg, rgba(0,0,0,0) 0 9px, rgba(120,50,10,0.35) 9px 11px),
      radial-gradient(ellipse at 50% 45%, var(--pretzel-light) 0%, #c9661c 60%, var(--pretzel-dark) 100%);
  }
  .product-name {
    position: absolute;
    left: 0;
    width: 1200px;
    top: 594px;
    text-align: center;
    font-family: "Cabin", sans-serif;
    font-weight: 500;
    font-size: 37px;
    color: var(--label-grey);
    text-shadow: 0 0 10px var(--glow), 0 0 18px var(--glow);
  }
  .net-weight {
    position: absolute;
    left: 0;
    width: 1300px;
    top: 664px;
    text-align: center;
    font-family: "Cabin", sans-serif;
    font-weight: 500;
    font-size: 29px;
    color: var(--weight-brown);
  }
</style>
</head>
<body>
<div class="canvas">
  <div class="landscape-artwork" role="img" aria-label="Sepia-toned rural landscape with sun rays over a forested hill, fields and a farmhouse"></div>

  <div class="spec-panel spec-panel--left"></div>
  <div class="spec-panel spec-panel--right"></div>

  <div class="brand-name">VOLK</div>

  <svg class="tagline-arc" viewBox="0 0 1200 1000">
    <defs>
      <path id="tagline-curve" d="M404,460 Q600,318 800,458"/>
    </defs>
    <text><textPath href="#tagline-curve" startOffset="50%" text-anchor="middle" textLength="420" lengthAdjust="spacing">Baked Golden Crispy!</textPath></text>
  </svg>

  <div class="product-window" role="img" aria-label="Window showing salted pretzel sticks"></div>

  <div class="product-name">Salted Pretzel Sticks</div>
  <div class="net-weight">400 g</div>
</div>
</body>
</html>
```